I need email signatures for my admin staff members
info:
Darina Qubrosi
Support Coordinator
Unit 4, 517 Wattlebrook Lane, Kemberly NSW 2893
Tel: 02 84427193 Mob: 0427596314
email: darina.qu@mivrotelhaven.com
www.mivrotelhaven.com

Target Market(s)

community services industry

Industry/Entity Type

Community Service

Requirements
Must have
• Specialist Provider of Multicultural Support Services
Nice to have
• "I acknowledge the traditional owners of the land on which we live, work and dream"
plus their flags as attached

```html
<!DOCTYPE html>
<html lang="en">
<head>
<meta charset="utf-8">
<title>Mivrotel Haven – Email Signature</title>
<link rel="stylesheet" href="https://fonts.googleapis.com/css2?family=Montserrat:ital,wght@0,400;0,500;0,700;0,800;1,500&display=swap">
<style>
  :root {
    --page: #ffffff;
    --orange: #f7941d;
    --charcoal: #333333;
    --text: #444444;
    --muted: #666666;
    --white: #ffffff;
    --icon: #9a9a9a;
    --flag-area-one: #8a1a12;
    --flag-area-two: #2a4fd6;
  }
  * { margin: 0; padding: 0; box-sizing: border-box; }
  html, body {
    width: 1151px; height: 1200px; overflow: hidden;
    background: var(--page);
    font-family: "Montserrat", Arial, sans-serif;
  }
  .canvas { position: relative; width: 1151px; height: 1200px; }
  .signature {
    position: absolute; left: 30px; top: 500px;
    width: 1211px; height: 222px;
    transform: scale(0.9); transform-origin: 0 0;
  }
  .signature-backdrop { position: absolute; inset: 0; }
  .brand { position: absolute; left: 10px; top: 0; width: 280px; text-align: center; }
  .brand-disc {
    display: block; margin: 1px auto 0; width: 98px; height: 98px;
    border-radius: 50%; background: var(--orange);
  }
  .brand-name {
    display: block; margin-top: 10px;
    font-size: 26px; font-weight: 500; color: var(--orange); letter-spacing: 0.5px;
  }
  .person {
    position: absolute; left: 329px; top: 41px; width: 451px;
    padding-bottom: 6px; border-bottom: 1.5px solid var(--muted);
    font-size: 21px; color: var(--muted); white-space: nowrap;
  }
  .person-name { font-weight: 700; color: var(--text); }
  .contact {
    position: absolute; left: 329px; top: 85px;
    font-size: 18.5px; line-height: 23px; color: var(--text); white-space: nowrap;
  }
  .social { position: absolute; left: 1026px; top: 5px; display: flex; gap: 42px; }
  .social-dot { width: 24px; height: 24px; border-radius: 50%; background: var(--icon); }
  .tagline { position: absolute; right: 26px; top: 74px; text-align: right; }
  .tagline-lead { font-size: 14px; color: var(--white); font-weight: 500; }
  .tagline-focus {
    font-size: 29px; line-height: 34px; font-weight: 800; color: var(--orange);
  }
  .acknowledgement {
    position: absolute; left: 12px; top: 177px;
    font-size: 22.5px; font-style: italic; font-weight: 500; color: var(--white); white-space: nowrap;
  }
  .flag-area { position: absolute; top: 168px; width: 74px; height: 43px; }
  .flag-area-aboriginal { left: 1024px; background: var(--flag-area-one); }
  .flag-area-torres { left: 1112px; background: var(--flag-area-two); }
</style>
</head>
<body>
<main class="canvas">
  <section class="signature" aria-label="Email signature">
    <svg class="signature-backdrop" width="1211" height="222" viewBox="0 0 1211 222" aria-hidden="true">
      <path fill="var(--charcoal)" d="M0,167 L860,167 Q875,167 884,154 L940,60 Q948,47 963,47 L1211,47 L1211,222 L0,222 Z"/>
    </svg>

    <div class="brand">
      <span class="brand-disc"></span>
      <span class="brand-name">MIVROTEL HAVEN</span>
    </div>

    <p class="person"><span class="person-name">Darina Qubrosi</span> - Support Coordinator</p>

    <div class="contact">
      <p>darina.qu@mivrotelhaven.com | www.mivrotelhaven.com</p>
      <p>Tel: 02 8442 7193 Mob: 0427 596 314</p>
      <p>Unit 4, 517 Wattlebrook Lane, Kemberly NSW 2893</p>
    </div>

    <div class="social" aria-label="Social links">
      <span class="social-dot"></span>
      <span class="social-dot"></span>
      <span class="social-dot"></span>
    </div>

    <div class="tagline">
      <p class="tagline-lead">Specialist Provider of</p>
      <p class="tagline-focus">Multicultural<br>Support Services</p>
    </div>

    <p class="acknowledgement">“I Acknowledge the traditional owners of the land on which we live, work and dream”</p>

    <div class="flag-area flag-area-aboriginal" role="img" aria-label="Aboriginal flag goes here"></div>
    <div class="flag-area flag-area-torres" role="img" aria-label="Torres Strait Islander flag goes here"></div>
  </section>
</main>
</body>
</html>
```